Fitness competition business needs a card design

I need a professional business card design using my logo. The card will be horizontal with rounded edges.

Target Market(s)

Female fitness competitors

Industry/Entity Type

Fitness

Contact Information for Business Card

Rose-Lynn Darby
Owner
stagevarno.com
555.301.2187
info@stagevarno.com

Font styles to use
Serif

Colors

Designer to choose colors to be used in the design.

Requirements
Must have
• On the back please add the following:
• Figure
• Bikini
• Physique
• Fitness
Nice to have
• Looking for a very sleek design, contemporary and easy to read.
Should not have
• Should not be difficult to read or be too busy

```html
<!DOCTYPE html>
<html lang="en">
<head>
<meta charset="utf-8">
<title>Stage Varno — Business Card</title>
<link rel="stylesheet" href="https://fonts.googleapis.com/css2?family=Lato:wght@300;400;700;900&display=swap">
<style>
  :root {
    --backdrop: #13263a;
    --card-white: #ffffff;
    --card-grey: #5a5a5b;
    --brand-red: #e02a2c;
    --ink-grey: #6f6f70;
    --text-light: #ffffff;
    --rule-light: #e6e6e6;
  }
  * { margin: 0; padding: 0; box-sizing: border-box; }
  html, body {
    width: 1200px; height: 1000px; overflow: hidden;
    background: var(--backdrop);
    font-family: "Lato", Arial, sans-serif;
  }
  .canvas { position: relative; width: 1200px; height: 1000px; }
  .card {
    position: absolute; left: 278px; width: 642px; height: 366px;
    border-radius: 40px;
  }
  .card--front { top: 98px; background: var(--card-white); }
  .card--back { top: 528px; background: var(--card-grey); color: var(--text-light); }

  .brand-name {
    position: absolute; left: 0; right: 0; top: 188px;
    text-align: center; font-weight: 900; font-size: 46px;
    letter-spacing: 2px; color: var(--brand-red); line-height: 1;
  }
  .disciplines {
    position: absolute; left: 0; right: 0; top: 312px;
    text-align: center; font-weight: 300; font-size: 22px;
    color: var(--ink-grey);
  }
  .disciplines .sep { color: var(--brand-red); margin: 0 6px; }

  .brand-name--small {
    position: absolute; right: 56px; top: 84px;
    font-weight: 900; font-size: 22px; letter-spacing: 1px;
    color: var(--text-light); line-height: 1;
  }
  .holder-name {
    position: absolute; left: 35px; top: 106px;
    font-weight: 400; font-size: 29px; line-height: 1;
  }
  .holder-role {
    position: absolute; left: 35px; top: 145px;
    font-weight: 400; font-size: 19px; line-height: 1;
  }
  .divider {
    position: absolute; left: 37px; top: 180px; width: 569px; height: 2px;
    background: var(--rule-light);
  }
  .contact {
    position: absolute; left: 34px; display: flex; align-items: center;
    font-size: 22px; letter-spacing: 1px; line-height: 1;
  }
  .contact svg { width: 20px; height: 20px; margin-right: 21px; fill: var(--text-light); }
  .contact--phone { top: 224px; }
  .contact--email { top: 259px; }
  .website {
    position: absolute; right: 40px; top: 321px;
    font-size: 18px; line-height: 1;
  }
</style>
</head>
<body>
<main class="canvas">
  <section class="card card--front">
    <div class="brand-name">STAGE VARNO</div>
    <p class="disciplines">Figure<span class="sep">|</span>Bikini<span class="sep">|</span>Physique<span class="sep">|</span>Fitness</p>
  </section>

  <section class="card card--back">
    <div class="brand-name--small">STAGE VARNO</div>
    <h1 class="holder-name">Rose-Lynn Darby</h1>
    <p class="holder-role">Owner</p>
    <div class="divider"></div>
    <p class="contact contact--phone">
      <svg viewBox="0 0 24 24" aria-hidden="true"><path d="M6.6 10.8a15.2 15.2 0 0 0 6.6 6.6l2.2-2.2a1 1 0 0 1 1-.25 11.4 11.4 0 0 0 3.6.6 1 1 0 0 1 1 1V20a1 1 0 0 1-1 1A17 17 0 0 1 3 4a1 1 0 0 1 1-1h3.5a1 1 0 0 1 1 1c0 1.25.2 2.45.6 3.6a1 1 0 0 1-.25 1z"/></svg>
      555.301.2187
    </p>
    <p class="contact contact--email">
      <svg viewBox="0 0 24 24" aria-hidden="true"><path d="M2 5h20v14H2z M3.5 6.5 12 13l8.5-6.5v-.2h-17z" fill-rule="evenodd"/><path d="M2 5h20L12 12.5z" fill="#5a5a5b" opacity=".35"/></svg>
      info@stagevarno.com
    </p>
    <p class="website">www.stagevarno.com</p>
  </section>
</main>
</body>
</html>
```